Create a Graphic About YOURSELF and PixelHarbor

PixelHarbor would like you (designers) to create an awesome graphic to promote YOURSELF and your profile on PixelHarbor!

Your graphic should communicate your name, your services and should mention PixelHarbor.

The design should be perfect for sharing on Chatterly. Here's an example of what we'd like http://blog.pixelharbor-example.ca/article/333/pixelharbor-launches-3000-hire-me-social-design-contest

Once you submitted your design, we'd love you to share the design ('advertisement') and promote yourself and PixelHarbor to your friends and potential customers. So make your submissions great and get your friends to vote for your design by 'Liking' it on Chatterly!

Prizes:
$1500 - "PixelHarbor Community" prize awarded to the designer with the most Chatterly 'Likes'
5 x $50 for the next 5 'most liked' designs on Chatterly

$1000 - "Hire Me" prize awarded to the designer who receives the most client invites
5 x $50 for the next 5 'most invited' designers

In summary, this is a great opportunity for you to increase your exposure to PixelHarbor customers and win cash prizes. Show off your design skills and get hired by PixelHarbor customers from around the world!

Target Market(s)

Fans, friends and customers of YOU

Industry/Entity Type

Cash

Requirements
Must have
• 1) Include your PixelHarbor user name on the graphic so customers can find you in the PixelHarbor Designer Directory
2) Include the tagline "Hire Me on PixelHarbor.com!" in your graphic design.
3) Share your design's URL on our Chatterly wall at http://chatterly-example.com/pixelharbor and get your friends to 'like' your design.
Nice to have
• 1) Include a tagline that expresses your design approach/philosophy
2) Artwork dimensions: 403 x 403 px
3) You can submit more than 1 design!
Should not have
• You must own the copyright of any images you use including stock imagery.

```html
<!DOCTYPE html>
<html lang="en">
<head>
<meta charset="utf-8">
<title>LumenCraftz – Hire Me on PixelHarbor</title>
<link rel="stylesheet" href="https://fonts.googleapis.com/css2?family=Pinyon+Script&family=Italianno&family=Oswald:wght@500;600&display=swap">
<style>
  :root {
    --paper: #eceae3;
    --paper-shade: #d9d8d2;
    --cloud: #f7f7f5;
    --water-deep: #3f86b4;
    --water-mid: #7fb6d6;
    --water-light: #c7e0ec;
    --title-blue: #3a86c2;
    --tagline-teal: #1f7585;
    --ink: #161616;
    --label: #ffffff;
    --splat-purple: #6b2b86;
    --splat-navy: #1e2150;
    --splat-rose: #c9384c;
    --splat-green: #2f9a4e;
    --splat-yellow: #e3ae2b;
    --splat-red: #c43b38;
    --brand-dark: #1b1f3a;
    --brand-dot: #1aa6c4;
    --portrait-dark: #2a2a2e;
  }
  * { box-sizing: border-box; margin: 0; padding: 0; }
  html, body { width: 1200px; height: 890px; overflow: hidden; background: var(--paper); }
  .canvas { position: relative; width: 1200px; height: 890px; overflow: hidden; }

  .backdrop {
    position: absolute; inset: 0;
    background:
      linear-gradient(160deg, transparent 0%, transparent 30%, var(--water-light) 36%, var(--water-mid) 42%, var(--water-deep) 47%, var(--water-mid) 53%, var(--water-light) 62%, transparent 72%),
      radial-gradient(ellipse at 30% 12%, var(--cloud) 0%, transparent 45%),
      radial-gradient(ellipse at 85% 30%, var(--cloud) 0%, transparent 40%),
      linear-gradient(180deg, var(--paper) 0%, var(--paper-shade) 100%);
  }

  .brand-title {
    position: absolute; left: 0; width: 100%; top: 48px;
    text-align: center;
    font-family: "Pinyon Script", cursive;
    font-size: 104px; line-height: 1;
    color: var(--title-blue);
  }
  .tagline {
    position: absolute; left: 0; width: 100%; top: 186px;
    text-align: center;
    font-family: "Italianno", cursive;
    font-size: 52px; line-height: 1;
    color: var(--tagline-teal);
  }

  .service {
    position: absolute;
    display: flex; align-items: center; justify-content: center;
    font-family: "Oswald", sans-serif; font-weight: 600;
    font-size: 32px; color: var(--label);
    letter-spacing: 0.5px;
  }
  .service--logos   { left: 40px;  top: 380px; width: 290px; height: 110px; background: var(--splat-purple); border-radius: 46% 54% 40% 60% / 55% 45% 55% 45%; }
  .service--flyers  { left: 470px; top: 395px; width: 220px; height: 95px;  background: var(--splat-navy);   border-radius: 50% 40% 55% 45% / 45% 55% 45% 55%; }
  .service--posters { left: 855px; top: 375px; width: 240px; height: 140px; background: var(--splat-rose);   border-radius: 40% 60% 50% 50% / 50% 40% 60% 50%; }
  .service--books   { left: 20px;  top: 540px; width: 370px; height: 100px; background: var(--splat-green);  border-radius: 30% 70% 45% 55% / 60% 40% 60% 40%; }
  .service--cds     { left: 410px; top: 560px; width: 240px; height: 140px; background: var(--splat-yellow); border-radius: 55% 45% 50% 50% / 45% 55% 45% 55%; }
  .service--banners { left: 740px; top: 600px; width: 180px; height: 86px;  background: var(--splat-red);    border-radius: 45% 55% 60% 40% / 55% 45% 55% 45%; }

  .site-address {
    position: absolute; left: 560px; top: 728px;
    font-family: "Italianno", cursive;
    font-size: 62px; line-height: 1; color: var(--ink);
  }
  .hire-line {
    position: absolute; left: 920px; top: 765px;
    font-family: "Oswald", sans-serif; font-weight: 600;
    font-size: 30px; line-height: 1; color: var(--ink);
  }
  .portrait {
    position: absolute; left: 1060px; top: 718px; width: 136px; height: 86px;
    background: radial-gradient(ellipse at 55% 50%, var(--portrait-dark) 0%, var(--portrait-dark) 35%, transparent 75%);
  }
  .platform {
    position: absolute; left: 684px; top: 806px;
    display: flex; align-items: center; gap: 14px;
  }
  .platform__dot { width: 62px; height: 62px; border-radius: 50%; background: var(--brand-dot); }
  .platform__name {
    font-family: "Oswald", sans-serif; font-weight: 600;
    font-size: 62px; line-height: 1; color: var(--brand-dark);
  }
</style>
</head>
<body>
<main class="canvas">
  <div class="backdrop" role="img" aria-label="Textured paper backdrop with soft clouds and a splashing blue water wave sweeping across"></div>

  <h1 class="brand-title">LumenCraftz</h1>
  <p class="tagline">Making Your Vision a Reality</p>

  <div class="service service--logos">Logos</div>
  <div class="service service--flyers">Flyers</div>
  <div class="service service--posters">Posters</div>
  <div class="service service--books">Book Covers</div>
  <div class="service service--cds">CD Covers</div>
  <div class="service service--banners">Banners</div>

  <p class="site-address">PixelHarbor.com</p>
  <p class="hire-line">HIRE ME ON</p>
  <div class="portrait" role="img" aria-label="Close-up photograph of the designer"></div>
  <div class="platform">
    <span class="platform__dot"></span>
    <span class="platform__name">PixelHarbor</span>
  </div>
</main>
</body>
</html>
```